Software Product Website Design

We have a software product which we have just renamed from Milestone Linked Tracking (MLT) to Norvessa. The web site is for www.norvessa-example.com and needs to contain certain information related to our software product in accordance with the information contained in the previous product brochure (see attached). The logo file is also attached but the designer is free to propose alternative logo colours. The theme for the website must be based on the selected logo colours..
Target Market(s)
Project Management, Engineering, Construction etc companies involved with projects in all industries world-wide
Industry/Entity Type
Software
Coding
Coded - Design and coding required
Number of Pages Required
1 page
Font styles to use
Requirements
Must have
- Professional but exciting theme. The contents of the attached brochure should be included.

```html
<!DOCTYPE html>
<html lang="en">
<head>
<meta charset="utf-8">
<title>Norvessa Software</title>
<link href="https://fonts.googleapis.com/css2?family=Raleway:wght@400;600;700;800&family=Open+Sans:wght@400;600;700&display=swap" rel="stylesheet">
<style>
:root{
  --blue:#3f9fd8;
  --blue-dark:#2f86bd;
  --footer-blue:#4aa6d8;
  --accent:#e2453a;
  --ink:#333a40;
  --muted:#7b8288;
  --line:#e3e6e8;
  --band:#f1f2f3;
  --bar:#2b2e31;
  --white:#ffffff;
}
*{box-sizing:border-box;margin:0;padding:0}
html,body{width:1200px;height:2216px;overflow:hidden}
body{font-family:"Open Sans",Arial,sans-serif;color:var(--ink);background:var(--white);position:relative}
h1,h2,h3,h4{font-family:"Raleway",Arial,sans-serif}

.site-header{position:absolute;left:0;top:0;width:1200px;height:92px;background:var(--white);display:flex;align-items:center;justify-content:space-between;padding:0 40px 0 28px;border-bottom:1px solid var(--line)}
.brand{display:flex;align-items:center;gap:12px;font-family:"Raleway",sans-serif;font-weight:700;font-size:30px;color:var(--ink)}
.brand-mark{width:34px;height:34px;background:var(--blue)}
.main-nav{display:flex;gap:4px}
.main-nav a{display:block;padding:14px 20px;font-size:13px;font-weight:600;letter-spacing:1px;color:var(--muted);text-decoration:none;text-transform:uppercase}
.main-nav a.active{background:var(--blue);color:var(--white)}

.hero{position:absolute;left:0;top:92px;width:1200px;height:668px;background:linear-gradient(120deg,#dfe6ea 0%,#b9c7cf 45%,#8fa3ad 100%)}
.hero-copy{position:absolute;left:110px;top:400px;width:700px}
.hero-copy h1{font-size:46px;line-height:54px;font-weight:800;color:var(--white);letter-spacing:1px;text-transform:uppercase;white-space:nowrap}
.hero-copy p{margin-top:12px;width:520px;font-size:26px;line-height:34px;color:var(--white);background:rgba(40,110,160,.55);padding:8px 14px;font-family:"Raleway",sans-serif}
.hero-arrows{position:absolute;left:110px;top:610px;display:flex;gap:6px}
.hero-arrows span{width:34px;height:34px;background:rgba(40,46,50,.7);display:flex;align-items:center;justify-content:center}

.section-title{text-align:center;font-size:30px;font-weight:700;letter-spacing:1px;text-transform:uppercase;color:var(--ink)}
.section-title em{font-style:normal;color:var(--accent)}
.welcome{position:absolute;left:0;top:815px;width:1200px}
.welcome p{width:760px;margin:20px auto 0;text-align:center;font-size:13px;line-height:22px;color:var(--muted)}

.features{position:absolute;left:80px;top:985px;width:1040px}
.features-head{display:flex;justify-content:space-between;align-items:center;border-bottom:1px solid var(--line);padding-bottom:12px}
.features-head h2{font-size:22px;font-weight:700;text-transform:uppercase}
.features-head h2 em{font-style:normal;color:var(--accent)}
.features-nav{display:flex;gap:6px}
.feature-grid{display:flex;gap:28px;margin-top:24px}
.feature{width:328px}
.feature-shot{height:110px;background:linear-gradient(180deg,#e9eef1,#c9d6dd);border:1px solid var(--line)}
.feature h3{margin-top:20px;font-size:15px;font-weight:700;text-transform:uppercase}
.feature p{margin-top:8px;font-size:12px;line-height:19px;color:var(--muted)}

.reporting{position:absolute;left:0;top:1300px;width:1200px;height:330px;background:var(--band)}
.reporting-art{position:absolute;left:240px;top:10px;width:310px;height:310px;background:radial-gradient(circle at 50% 45%,#6fb5e3 0%,#3d88c0 45%,#dfe6ea 75%)}
.reporting-copy{position:absolute;left:600px;top:44px;width:500px}
.reporting-copy h2{font-size:24px;font-weight:700;text-transform:uppercase}
.reporting-copy h2 em{font-style:normal;color:var(--accent)}
.reporting-copy p{margin-top:14px;font-size:12px;line-height:20px;color:var(--muted)}
.btn{display:inline-block;margin-top:20px;padding:10px 22px;background:var(--blue);color:var(--white);font-size:11px;font-weight:700;letter-spacing:1px;text-transform:uppercase}

.testimonials{position:absolute;left:0;top:1660px;width:1200px}
.testimonials .section-title{font-size:24px}
.testimonial-row{display:flex;gap:40px;width:1020px;margin:40px auto 0}
.testimonial{flex:1;display:flex;gap:30px}
.testimonial-photo{width:110px;height:110px;border-radius:50%;background:linear-gradient(160deg,#d9dde0,#9aa4aa);flex:none}
.testimonial-body{position:relative;padding-top:6px}
.quote{position:absolute;left:-24px;top:0;font-family:Georgia,serif;font-size:36px;line-height:1;color:#b8bec2}
.testimonial-body p{font-size:12px;line-height:19px;color:var(--muted)}
.testimonial-body h4{margin-top:10px;font-size:11px;font-weight:700;color:var(--blue);text-transform:uppercase}
.testimonial-body .role{font-size:11px;color:var(--muted)}

.site-footer{position:absolute;left:0;top:1925px;width:1200px;height:223px;background:var(--footer-blue);color:var(--white)}
.footer-brand{position:absolute;left:120px;top:46px;display:flex;align-items:center;gap:10px;font-family:"Raleway",sans-serif;font-weight:700;font-size:22px}
.footer-brand .brand-mark{width:26px;height:26px;background:var(--white)}
.footer-cols{position:absolute;left:310px;top:40px;display:flex;gap:58px}
.footer-cols h4{font-size:13px;font-weight:700;text-transform:uppercase;letter-spacing:1px}
.footer-cols ul{list-style:none;margin-top:14px}
.footer-cols li{font-size:12px;line-height:22px;opacity:.9}
.footer-cols .contact{width:240px}

.bottom-bar{position:absolute;left:0;top:2148px;width:1200px;height:68px;background:var(--bar);color:#c9ced2;font-size:11px;padding:16px 120px;display:flex;justify-content:space-between;align-items:center}
.bottom-bar p{line-height:18px}
.social{display:flex;gap:6px}
.social span{width:22px;height:22px;background:var(--blue)}
.social span:nth-child(2){background:#3b5b98}
.social span:nth-child(3){background:#d6453a}
.social span:nth-child(4){background:#3178b2}
.social span:nth-child(5){background:#c7302a}
</style>
</head>
<body>

<header class="site-header">
  <div class="brand"><span class="brand-mark"></span>Norvessa</div>
  <nav class="main-nav">
    <a class="active">Home</a><a>About Us</a><a>Services</a><a>Blog</a><a>Portfolio</a><a>News</a><a>Contact</a>
  </nav>
</header>

<section class="hero" role="img" aria-label="Hands holding a tablet showing analytics charts above a desk with reports">
  <div class="hero-copy">
    <h1>Norvessa Software</h1>
    <p>Lorem Ipsum is simply dummy text of the printing and typesetting industry.</p>
  </div>
  <div class="hero-arrows">
    <span><svg width="12" height="12" viewBox="0 0 12 12"><path d="M8 1L3 6l5 5" stroke="#fff" stroke-width="2" fill="none"/></svg></span>
    <span><svg width="12" height="12" viewBox="0 0 12 12"><path d="M4 1l5 5-5 5" stroke="#fff" stroke-width="2" fill="none"/></svg></span>
  </div>
</section>

<section class="welcome">
  <h2 class="section-title">Welcome to <em>Norvessa</em></h2>
  <p>Lorem Ipsum has been the industry's standard dummy text ever since the 1500s, when an unknown printer took a galley of type and scrambled it to make a type specimen book. It has survived not only five centuries, but also the leap into electronic typesetting, remaining essentially unchanged. It was popularised in the 1960s with the release of Letraset sheets containing Lorem Ipsum passages, and more recently with desktop publishing software.</p>
</section>

<section class="features">
  <div class="features-head">
    <h2>Feature <em>Product</em></h2>
    <div class="features-nav">
      <svg width="14" height="14" viewBox="0 0 12 12"><path d="M8 1L3 6l5 5" stroke="#7b8288" stroke-width="2" fill="none"/></svg>
      <svg width="14" height="14" viewBox="0 0 12 12"><path d="M4 1l5 5-5 5" stroke="#7b8288" stroke-width="2" fill="none"/></svg>
    </div>
  </div>
  <div class="feature-grid">
    <article class="feature">
      <div class="feature-shot" role="img" aria-label="Screenshot of the dashboard view with charts and tables"></div>
      <h3>Dashboard</h3>
      <p>Lorem Ipsum has been the industry's standard dummy text ever since the 1500s, when an unknown printer took a galley.</p>
    </article>
    <article class="feature">
      <div class="feature-shot" role="img" aria-label="Screenshot of the metrics view with bar charts"></div>
      <h3>Metrics</h3>
      <p>Lorem Ipsum has been the industry's standard dummy text ever since the 1500s, when an unknown printer took a galley.</p>
    </article>
    <article class="feature">
      <div class="feature-shot" role="img" aria-label="Screenshot of the tabular report view"></div>
      <h3>Tabular Report</h3>
      <p>Lorem Ipsum has been the industry's standard dummy text ever since the 1500s, when an unknown printer took a galley.</p>
    </article>
  </div>
</section>

<section class="reporting">
  <div class="reporting-art" role="img" aria-label="Tablet with a glowing globe representing worldwide project tracking"></div>
  <div class="reporting-copy">
    <h2>Milestone <em>Linked Tracking</em></h2>
    <p>Lorem Ipsum has been the industry's standard dummy text ever since the 1500s, when an unknown printer took a galley of type and scrambled it to make a type specimen book. It has survived not only five centuries, but also the leap into electronic typesetting.</p>
    <p>Remaining essentially unchanged. It was popularised in the 1960s with the release of Letraset sheets containing Lorem Ipsum passages, and more recently with desktop publishing software including versions of Lorem Ipsum.</p>
    <span class="btn">Read More</span>
  </div>
</section>

<section class="testimonials">
  <h2 class="section-title">Testimonials</h2>
  <div class="testimonial-row">
    <div class="testimonial">
      <div class="testimonial-photo" role="img" aria-label="Portrait photo of a client"></div>
      <div class="testimonial-body"><span class="quote">&ldquo;</span>
        <p>Lorem Ipsum is simply dummy text of the printing and typesetting industry.</p>
        <h4>Daniel Harrow</h4><span class="role">Marketing Executive</span></div>
    </div>
    <div class="testimonial">
      <div class="testimonial-photo" role="img" aria-label="Portrait photo of a client"></div>
      <div class="testimonial-body"><span class="quote">&ldquo;</span>
        <p>Lorem Ipsum is simply dummy text of the printing and typesetting industry.</p>
        <h4>Elena Marsh</h4><span class="role">Marketing Executive</span></div>
    </div>
    <div class="testimonial">
      <div class="testimonial-photo" role="img" aria-label="Portrait photo of a client"></div>
      <div class="testimonial-body"><span class="quote">&ldquo;</span>
        <p>Lorem Ipsum is simply dummy text of the printing and typesetting industry.</p>
        <h4>Owen Castell</h4><span class="role">Marketing Executive</span></div>
    </div>
  </div>
</section>

<footer class="site-footer">
  <div class="footer-brand"><span class="brand-mark"></span>Norvessa</div>
  <div class="footer-cols">
    <div><h4>Link</h4><ul><li>About Us</li><li>Services</li><li>Presentations</li></ul></div>
    <div><h4>Advice</h4><ul><li>FAQs</li><li>Support</li><li>Resources</li></ul></div>
    <div><h4>Agencies</h4><ul><li>Sign Up</li><li>Partners</li><li>Promotions</li></ul></div>
    <div class="contact"><h4>Contact Us</h4><ul><li>1420 Harbour Road, Westmere, 90210</li><li>Phone: +1 555 0148 2260</li><li>E-mail: info@norvessa-example.com</li></ul></div>
  </div>
</footer>

<div class="bottom-bar">
  <div><p>Privacy Policy &nbsp;|&nbsp; Terms of Use &nbsp;|&nbsp; About Us &nbsp;|&nbsp; Sitemap</p><p>Copyright &copy; 2016. All Rights Reserved.</p></div>
  <div class="social"><span></span><span></span><span></span><span></span><span></span></div>
</div>

</body>
</html>
```